Business Card Design Project

I am community manager and social media strategist. I need a double sided business card with company logo and name. Looking for something professional, elegant but also a little bit original.

• - The logo and the colours are the company colours and a required to stay.
- The size should be: 84 x 55 mm (or 3.30 x 2.16)
- The file size should be: 1039 x 697 pixels (300 dpi)
- I'd like rounded corners. :)

Use the following contact information for the card:

Léonie Vardin
Stratégie médias sociaux / community management / édition de sites sociaux
mob. : 0687529103
leonie.vardin@postelune.fr
Twitter. : @lvardin
Skype : vardin.leonie

```html
<!DOCTYPE html>
<html lang="fr">
<head>
<meta charset="utf-8">
<title>Ventelis – cartes de visite</title>
<link rel="stylesheet" href="https://fonts.googleapis.com/css2?family=Barlow:wght@400;500;600&display=swap">
<style>
  :root {
    --brand-deep: #0b558f;
    --brand-mid: #135f9c;
    --brand-light: #1a82bf;
    --brand-text: #0d5a96;
    --paper: #ffffff;
    --muted: #9a9a9a;
    --rule: #a8a8a8;
    --canvas: #ffffff;
  }
  html, body {
    margin: 0;
    padding: 0;
    width: 1200px;
    height: 900px;
    overflow: hidden;
    background: var(--canvas);
    font-family: "Barlow", "Helvetica Neue", Arial, sans-serif;
  }
  .stage {
    position: relative;
    width: 1200px;
    height: 900px;
  }
  .card {
    position: absolute;
    width: 505px;
    height: 330px;
    border-radius: 46px;
    overflow: hidden;
    background: linear-gradient(100deg, var(--brand-deep) 0%, var(--brand-mid) 45%, var(--brand-light) 100%);
    box-shadow: 10px 12px 14px rgba(0, 0, 0, 0.45);
  }
  .card--front { left: 60px; top: 284px; }
  .card--back  { left: 636px; top: 286px; height: 328px; }

  .card__panel {
    position: absolute;
    left: 0;
    right: 0;
    background: var(--paper);
  }
  .card--front .card__panel { top: 79px; height: 175px; }
  .card--back  .card__panel { top: 77px; height: 175px; }

  /* Front: brand name */
  .brand {
    position: absolute;
    left: 0;
    right: 0;
    top: 0;
    height: 100%;
    display: flex;
    align-items: center;
    justify-content: center;
    gap: 14px;
  }
  .brand__dot {
    width: 26px;
    height: 26px;
    border-radius: 50%;
    background: var(--brand-light);
  }
  .brand__name {
    font-weight: 600;
    font-size: 40px;
    letter-spacing: 2px;
    color: var(--brand-text);
  }

  /* Back: identity */
  .identity {
    position: absolute;
    right: 259px;
    top: 108px;
    text-align: right;
    color: var(--brand-text);
  }
  .identity__name {
    margin: 0 0 2px;
    font-weight: 500;
    font-size: 38px;
    line-height: 40px;
    letter-spacing: 0.5px;
  }
  .identity__roles {
    margin: 0;
    padding: 0;
    list-style: none;
    font-size: 18px;
    line-height: 23px;
    letter-spacing: 0.3px;
  }
  .divider {
    position: absolute;
    left: 265px;
    top: 107px;
    width: 2px;
    height: 115px;
    background: var(--rule);
  }
  .contacts {
    position: absolute;
    left: 282px;
    top: 119px;
    margin: 0;
    padding: 0;
    list-style: none;
    font-size: 17.5px;
    line-height: 25.5px;
    color: var(--muted);
    letter-spacing: 0.3px;
  }
  .footer-line {
    position: absolute;
    left: 0;
    right: 0;
    top: 258px;
    text-align: center;
    font-size: 15.5px;
    color: var(--paper);
    letter-spacing: 0.5px;
    opacity: 0.95;
  }
  .footer-line strong { font-weight: 600; }
</style>
</head>
<body>
<main class="stage">
  <section class="card card--front" aria-label="Recto">
    <div class="card__panel">
      <div class="brand">
        <span class="brand__dot"></span>
        <span class="brand__name">VENTELIS</span>
      </div>
    </div>
  </section>

  <section class="card card--back" aria-label="Verso">
    <div class="card__panel"></div>
    <div class="identity">
      <h1 class="identity__name">Léonie Vardin</h1>
      <ul class="identity__roles">
        <li>Stratégie médias sociaux</li>
        <li>Community management</li>
        <li>Édition de sites sociaux</li>
      </ul>
    </div>
    <div class="divider"></div>
    <ul class="contacts">
      <li>mob. 0687529103</li>
      <li>leonie.vardin@postelune.fr</li>
      <li>Twitter @lvardin</li>
      <li>Skype vardin.leonie</li>
    </ul>
    <p class="footer-line" style="margin:0">leonie.vardin@postelune.fr | <strong>Twitter</strong> @lvardin | <strong>Skype</strong> vardin.leonie</p>
  </section>
</main>
</body>
</html>
```